Vormsted Off-Grid Energy

The company provides world wide installations and products for off-grid energy solutions. This means AC power where there is no network available. Mostly this is with solar panels combined with hybrid inverters and Lithium batteries. In the future small windmills and hydropower. The company is Dutch but has a hub in Hungary to supply the Balkan and surrounding countries.

We sell all Koru products and also Pinewatt and Lumask energy products

I have 3 versions of my logo. 2 attached and the third is the Off-grid energy text in black. Just see what works best with the design.
Obviously I need a good design but also good coding. It needs to meet al the latest (Google) search engine standards and should heave a web shop.
The web shop should be able to work with different currencies and calculate international shipping fees. Orders should be paid with; credit card, Quidflow, Fenpay or whatever is used internationally.

Coding

Number of Pages Required

5+ page

Font styles to use
Other font styles liked:
• see logo

Colors
0054AA
0677BA
7BADD7
CADEEF
E8F1F8
0094D4
00A9DD
6FCCEA
C7EBF8
E9F6FB
59FF00
82FF00
B8FF75
E3FFCB
F4FFEA
EB3D1F
EC4F4E
F09395
F8D3D4
FCEDEE

Requirements
Must have
• web shop
Nice to have
• slick design
Should not have
• stupid things ;-)

```html
<!DOCTYPE html>
<html lang="en">
<head>
<meta charset="utf-8">
<title>Vormsted Off-Grid Energy</title>
<link href="https://fonts.googleapis.com/css2?family=Lexend:wght@300;400;500;600;700&display=swap" rel="stylesheet">
<style>
  :root{
    --blue:#0054AA;
    --blue-mid:#0677BA;
    --blue-soft:#7BADD7;
    --blue-pale:#E8F1F8;
    --lime:#82FF00;
    --lime-soft:#B8FF75;
    --ink:#0F1228;
    --navy:#0B1530;
    --grey:#7A8194;
    --line:#DDE1E8;
    --bar:#F1F3F7;
    --white:#FFFFFF;
    --forest:#134236;
  }
  *{box-sizing:border-box;margin:0;padding:0}
  html,body{width:1200px;height:1200px;overflow:hidden}
  body{position:relative;background:var(--white);font-family:"Lexend",sans-serif;color:var(--ink)}
  .abs{position:absolute}

  /* Why choose us */
  .why-photo{left:214px;top:46px;width:464px;height:179px;background:linear-gradient(120deg,#5f7a5a 0%,#8a9b8a 40%,#c8cfd6 70%,#3f4a5a 100%)}
  .eyebrow{left:711px;top:42px;font-size:9.5px;font-weight:600;color:var(--blue);letter-spacing:.2px;display:flex;align-items:center;gap:5px}
  .eyebrow .dot{width:9px;height:9px;border-radius:50%;background:var(--blue-mid)}
  .why-title{left:711px;top:64px;font-size:31px;font-weight:600;color:var(--ink)}
  .why-text{left:711px;top:113px;width:275px;font-size:10.5px;line-height:17px;color:var(--grey);font-weight:300}
  .why-rule{left:711px;top:179px;width:267px;height:1px;background:var(--line)}
  .why-check{left:711px;top:198px;display:flex;align-items:center;gap:10px;font-size:10px;color:var(--ink)}
  .tick{width:16px;height:16px;background:var(--blue);display:flex;align-items:center;justify-content:center}

  /* Top bar */
  .topbar{left:137px;top:322px;width:926px;height:32px;background:var(--bar);font-size:10px;color:var(--ink)}
  .topbar span{position:absolute;top:10px}
  .social{position:absolute;top:10px;width:12px;height:12px;border-radius:50%;background:var(--navy)}

  /* Hero */
  .hero{left:137px;top:354px;width:926px;height:509px;background:var(--blue);overflow:hidden}
  .logo-pill{left:79px;top:21px;width:105px;height:42px;border-radius:21px;background:var(--white);display:flex;align-items:center;justify-content:center;gap:6px;font-size:13px;font-weight:600;color:var(--ink)}
  .logo-pill i{width:10px;height:10px;background:var(--lime);display:block}
  .nav a{position:absolute;top:36px;font-size:9.5px;font-weight:600;color:var(--white);text-decoration:none}
  .nav a.active{color:var(--lime)}
  .talk{left:756px;top:24px;width:91px;height:35px;border-radius:18px;background:var(--lime-soft);font-size:9px;font-weight:600;color:var(--ink);display:flex;align-items:center;justify-content:center}
  .hero-title{left:82px;top:142px;font-size:41px;line-height:52px;font-weight:600;color:var(--white)}
  .hero-title em{font-style:normal;color:var(--lime)}
  .hero-text{left:82px;top:310px;width:355px;font-size:10px;line-height:17px;color:var(--white);font-weight:300}
  .cta{left:81px;top:375px;width:195px;height:34px;border-radius:17px;background:var(--white);font-size:9px;font-weight:600;color:var(--ink);display:flex;align-items:center;justify-content:center}
  .play{left:296px;top:375px;width:34px;height:34px;border-radius:50%;background:var(--navy);display:flex;align-items:center;justify-content:center}
  .play-label{left:340px;top:380px;font-size:7.5px;line-height:11px;color:var(--white)}
  .grid-lines{left:0;top:0}
  .stat{left:525px;top:118px;width:111px;height:91px;background:var(--ink);color:var(--white);padding:16px 0 0 18px}
  .stat b{display:block;font-size:24px;font-weight:600}
  .stat small{display:block;font-size:7px;line-height:9px;margin-top:4px;color:#c9cde0;width:60px}
  .projects-link{left:705px;top:144px;font-size:8.5px;font-weight:500;color:var(--white);border-bottom:1px solid var(--blue-soft);padding-bottom:3px}
  .hero-photo{left:556px;top:184px;width:256px;height:251px;background:linear-gradient(180deg,#6d8fb8 0%,#9bb3cf 30%,#c9c7c2 55%,#4f7a3a 80%,#3a5f2b 100%)}

  /* Shop */
  .search-label{left:213px;top:1049px;font-size:11px;font-weight:600;color:var(--forest)}
  .search-box{left:213px;top:1077px;width:206px;height:37px;border:1px solid var(--line);border-radius:19px;font-size:10px;color:var(--grey);padding:12px 0 0 16px}
  .search-box svg{position:absolute;right:13px;top:11px}
  .side-card{left:213px;top:1137px;width:206px;height:80px;background:var(--white);box-shadow:0 2px 14px rgba(15,18,40,.07)}
  .side-card span{position:absolute;left:20px;top:30px;font-size:12px;font-weight:600;color:var(--blue)}
  .side-card svg{position:absolute;right:20px;top:33px}
  .brand-text{left:449px;top:1080px;width:345px;font-size:10.5px;line-height:19px;color:var(--grey);font-weight:300}
  .brand-box{left:843px;top:1054px;width:141px;height:73px;border:1px solid #c9ccd4;display:flex;align-items:center;justify-content:center;font-size:28px;font-weight:600;color:var(--blue)}
  .product{top:1137px;width:263px;height:90px;border:1px solid #cfd3da;border-radius:10px;overflow:hidden}
  .product .thumb{position:absolute;left:10px;top:12px;width:103px;height:80px;background:linear-gradient(90deg,#eceef1,#d7dbe0)}
  .product h3{position:absolute;left:125px;top:34px;font-size:11px;line-height:17px;font-weight:600;color:var(--blue)}
</style>
</head>
<body>

<section class="why">
  <div class="abs why-photo" role="img" aria-label="Photo of two engineers in hard hats in front of a solar panel field"></div>
  <p class="abs eyebrow"><span class="dot"></span>RELIABLE ENERGY SOLUTIONS FOR EVERY LOCATION</p>
  <h2 class="abs why-title">Why Choose Us?</h2>
  <p class="abs why-text">Advanced off-grid energy systems for homes, businesses, and industries—designed for efficiency, reliability, and long-term performance.</p>
  <div class="abs why-rule"></div>
  <div class="abs why-check">
    <span class="tick"><svg width="9" height="9" viewBox="0 0 10 10"><path d="M1.5 5.2 4 7.6 8.6 2.4" fill="none" stroke="#fff" stroke-width="1.5"/></svg></span>
    100% Off-Grid Independence
  </div>
</section>

<header class="abs topbar">
  <span style="left:96px">48 Harbor Lane, NY</span>
  <span style="left:253px">hi@vormsted.com</span>
  <span style="left:377px">+1 (555) 010-2040</span>
  <i class="social" style="left:740px"></i>
  <i class="social" style="left:778px"></i>
  <i class="social" style="left:816px"></i>
</header>

<section class="abs hero">
  <svg class="abs grid-lines" width="926" height="509" aria-hidden="true">
    <g stroke="#7BADD7" stroke-width="1" stroke-dasharray="3 4" opacity=".6">
      <line x1="470" y1="141" x2="525" y2="141"/>
      <line x1="470" y1="253" x2="556" y2="253"/>
      <line x1="470" y1="359" x2="556" y2="359"/>
      <line x1="812" y1="141" x2="860" y2="141"/>
      <line x1="505" y1="110" x2="505" y2="400"/>
      <line x1="669" y1="55" x2="669" y2="184"/>
      <line x1="705" y1="55" x2="705" y2="140"/>
    </g>
  </svg>
  <div class="abs logo-pill"><i></i>Vormsted</div>
  <nav class="nav">
    <a class="active" style="left:398px">Home</a>
    <a style="left:445px">About Us</a>
    <a style="left:506px">Services</a>
    <a style="left:565px">Projects</a>
    <a style="left:622px">Pricing</a>
    <a style="left:674px">Contact Us</a>
  </nav>
  <div class="abs talk">LET'S TALK</div>
  <h1 class="abs hero-title">Powering Your<br>Freedom with<br><em>Off-Grid Energy</em></h1>
  <p class="abs hero-text">Reliable. Sustainable. Anywhere. Vormsted provides premium off-grid energy solutions for homes, businesses, and industries worldwide.</p>
  <div class="abs cta">REQUEST A FREE CONSULTATION</div>
  <div class="abs play"><svg width="10" height="10" viewBox="0 0 10 10"><path d="M2 1 9 5 2 9Z" fill="#fff"/></svg></div>
  <p class="abs play-label">Let's See<br>How It Works</p>
  <div class="abs hero-photo" role="img" aria-label="Photo of two engineers with hard hats and plans beside solar panels"></div>
  <div class="abs stat"><b>20%</b><small>Increase Clean Energy</small></div>
  <p class="abs projects-link">SEE OUR LATEST PROJECTS</p>
</section>

<section class="shop">
  <p class="abs search-label">Search</p>
  <div class="abs search-box">Search Here
    <svg width="13" height="13" viewBox="0 0 14 14"><circle cx="6" cy="6" r="4.5" fill="none" stroke="#134236" stroke-width="1.5"/><line x1="9.4" y1="9.4" x2="13" y2="13" stroke="#134236" stroke-width="1.5"/></svg>
  </div>
  <div class="abs side-card"><span>Koru Inverters</span>
    <svg width="7" height="10" viewBox="0 0 7 10"><path d="M1.5 1 5.5 5 1.5 9" fill="none" stroke="#0054AA" stroke-width="1.4"/></svg>
  </div>
  <p class="abs brand-text">Koru specializes in high-efficiency hybrid inverters, ensuring reliable off-grid power for homes, businesses, and industries.</p>
  <div class="abs brand-box">Koru</div>
  <article class="abs product" style="left:449px">
    <div class="thumb" role="img" aria-label="Product photo of a white string inverter"></div>
    <h3>Single Phase String<br>Inverter</h3>
  </article>
  <article class="abs product" style="left:725px">
    <div class="thumb" role="img" aria-label="Product photo of a white string inverter"></div>
    <h3>Single Phase String<br>Inverter</h3>
  </article>
</section>

</body>
</html>
```